Beautiful e-comm site for 'roadside farmers stand' online!

Need a logo design and basic e-comm website (super super simple) for new business called Brindlecove. Brindlecove is an online farmers stand where local artisans can sell 'brindlecove' goods directly from their makers!

Looking for something simple, whimsicle and clean! (Ideally with a light grey or perrywinkle and some color mixed in - word 'Brindlecove' in black - can work the pear shape in somewhere but not required!)

Target Market(s)

Hobby shoppers and 'quilo' goers who want a focus on edible things and care about ingredients!

Industry/Entity Type

E-Commerce

Number of Pages Required

2 page

Font styles to use
Decorative
Script

Colors
f3f1f8
ec1f27
cadf82

Requirements
Must have
• - Basic logo
• - Homepage
• - Product Detail Page
• - Be in a responsive, woocommerce or shopify, wordpress theme (will purchase theme after design is approved)
Nice to have
• - Matching check out & cart pages
• - 'About Us' page
• - SEO plugin
Should not have
• A cluttered look/feel.

```html
<!DOCTYPE html>
<html lang="en">
<head>
<meta charset="utf-8">
<title>Brindlecove – Strawberry Jam</title>
<link href="https://fonts.googleapis.com/css2?family=Rosario:wght@400;600;700&family=Lobster&display=swap" rel="stylesheet">
<style>
  :root {
    --ink: #111111;
    --text: #333333;
    --muted: #555555;
    --red: #ec1f27;
    --lime: #cadf82;
    --lavender: #f3f1f8;
    --rule: #e6e6e6;
    --pink: #e8197d;
    --star: #f4a81d;
    --orange: #f26b1d;
  }
  * { box-sizing: border-box; margin: 0; padding: 0; }
  html, body { width: 708px; height: 1200px; overflow: hidden; }
  body {
    position: relative;
    background: #ffffff;
    font-family: "Rosario", sans-serif;
    color: var(--text);
  }
  .abs { position: absolute; }
  .rule { position: absolute; height: 1px; background: var(--rule); }

  /* header */
  .brand { font-weight: 700; color: var(--ink); font-size: 21px; display: flex; align-items: center; gap: 4px; }
  .brand-dot { width: 6px; height: 6px; border-radius: 50%; background: var(--red); }
  .top-link { font-size: 8.5px; color: var(--ink); top: 21px; }
  .top-link.cart { color: var(--red); display: flex; align-items: center; gap: 3px; }
  .cat-nav { top: 58px; font-size: 8.5px; color: var(--ink); }
  .cat-nav.active { color: #a9c84a; }

  /* product info */
  .title { left: 66px; top: 104px; width: 270px; font-size: 15px; line-height: 17px; color: var(--ink); font-weight: 400; }
  .price { left: 68px; top: 146px; font-size: 12px; color: var(--ink); }
  .add-btn {
    left: 101px; top: 174px; width: 202px; height: 19px;
    background: var(--red); color: #fff; border-radius: 2px;
    font-size: 8px; font-weight: 700;
    display: flex; align-items: center; justify-content: center; gap: 4px;
  }
  .section-head { font-size: 8px; font-weight: 700; color: var(--ink); }
  .bullets { list-style: none; font-size: 7px; line-height: 10.2px; color: var(--text); }
  .bullets li { position: relative; padding-left: 17px; }
  .bullets li::before {
    content: ""; position: absolute; left: 5px; top: 4px;
    width: 2.5px; height: 2.5px; border-radius: 50%; background: var(--pink);
  }
  .stars { color: var(--star); letter-spacing: -1px; font-size: 8px; margin-right: 3px; }
  .heart { color: var(--red); margin-right: 4px; }
  .desc { left: 66px; top: 368px; width: 272px; font-size: 7.4px; line-height: 8.6px; color: var(--text); }
  .desc p { margin-bottom: 8.6px; }
  .more { left: 66px; top: 522px; font-size: 7.5px; font-weight: 700; color: var(--orange); }

  /* gallery */
  .hero-photo {
    left: 354px; top: 107px; width: 304px; height: 263px;
    background: linear-gradient(180deg, #86b84a 0%, #5f9431 45%, #8a4a2e 80%, #a07048 100%);
  }
  .fav {
    left: 365px; top: 118px; width: 19px; height: 19px; border-radius: 50%;
    background: #fff; display: flex; align-items: center; justify-content: center;
  }
  .zoom {
    left: 631px; top: 345px; width: 17px; height: 17px; border-radius: 3px;
    background: rgba(255,255,255,.6); display: flex; align-items: center; justify-content: center;
  }
  .thumb { top: 386px; width: 40px; height: 40px; border: 1px solid #ddd; }
  .t1 { left: 394px; background: linear-gradient(135deg, #c44 0%, #e9b9b0 100%); }
  .t2 { left: 440px; background: linear-gradient(135deg, #f4e6e2 0%, #d8232a 80%); }
  .t3 { left: 486px; background: linear-gradient(160deg, #a36a3a 0%, #7a1418 80%); }
  .t4 { left: 531px; background: linear-gradient(160deg, #8cc050 0%, #c42a2a 90%); }
  .t5 { left: 577px; background: linear-gradient(160deg, #e94d5a 0%, #6b1016 80%); }

  .ship-item { left: 354px; top: 472px; }
  .share-icon { top: 508px; width: 18px; height: 18px; border-radius: 3px; }
  .pay-card {
    top: 570px; width: 26px; height: 19px; border: 1px solid #ccc; border-radius: 2px;
    font-size: 5px; font-weight: 700; color: var(--ink);
    display: flex; align-items: center; justify-content: center;
  }

  /* similar products */
  .similar-head { left: 0; width: 708px; text-align: center; top: 624px; font-size: 10.5px; color: var(--ink); font-weight: 400; }
  .card { top: 652px; width: 81px; }
  .card-photo { width: 81px; height: 79px; }
  .card-name { margin-top: 5px; font-size: 7px; line-height: 8px; color: var(--ink); }
  .card-price { margin-top: 3px; font-size: 7px; font-weight: 700; color: var(--ink); }

  /* newsletter */
  .news-band {
    left: 0; top: 836px; width: 708px; height: 202px;
    background: linear-gradient(180deg, #4f6f9a 0%, #a9b9cc 35%, #d9dfe6 48%, #3f6a26 62%, #7fae3a 80%, #a9cc4a 100%);
  }
  .news-label {
    left: 302px; top: 822px; width: 100px; height: 27px; background: #fff;
    border: 1.5px solid var(--lime); font-family: "Lobster", cursive; font-size: 17px;
    color: var(--ink); display: flex; align-items: center; justify-content: center;
  }
  .news-title { left: 0; width: 708px; text-align: center; top: 880px; font-size: 14px; color: #fff; }
  .news-sub { left: 0; width: 708px; text-align: center; top: 900px; font-size: 10px; color: #fff; }
  .news-form { left: 201px; top: 926px; width: 301px; height: 28px; background: #fff; display: flex; }
  .news-input { flex: 1; font-size: 9px; color: #777; padding-left: 11px; display: flex; align-items: center; }
  .news-btn {
    width: 61px; margin: 2px; background: var(--red); color: #fff; font-size: 9px; font-weight: 700;
    display: flex; align-items: center; justify-content: center;
  }

  /* footer */
  .footer { left: 0; top: 1038px; width: 708px; height: 162px; background: var(--lavender); }
  .footer-brand { left: 0; width: 708px; top: 1069px; justify-content: center; }
  .social { top: 1110px; width: 22px; height: 22px; border-radius: 50%; background: var(--red);
    color: #fff; font-size: 6px; font-weight: 700; display: flex; align-items: center; justify-content: center; }
  .copyright { left: 0; width: 708px; text-align: center; top: 1147px; font-size: 8px; color: var(--text); }
</style>
</head>
<body>

<header>
  <div class="abs brand" style="left:51px; top:12px;"><span>Brindlecove</span><span class="brand-dot"></span></div>
  <a class="abs top-link" style="left:482px;">About Us</a>
  <a class="abs top-link" style="left:538px;">Register</a>
  <a class="abs top-link" style="left:585px;">Sign In</a>
  <a class="abs top-link cart" style="left:626px;">
    <svg width="10" height="8" viewBox="0 0 10 8"><path d="M0 0.5h1.8l1.4 5h5.2l1.1-3.8H2.6" fill="none" stroke="#ec1f27" stroke-width="1.2"/><circle cx="3.8" cy="7.2" r=".8" fill="#ec1f27"/><circle cx="7.8" cy="7.2" r=".8" fill="#ec1f27"/></svg>Cart</a>
  <div class="rule" style="left:0; top:50px; width:708px;"></div>
  <nav>
    <span class="abs cat-nav" style="left:142px;">Homemade Products:</span>
    <a class="abs cat-nav active" style="left:253px;">Jams</a>
    <a class="abs cat-nav" style="left:298px;">Jellies</a>
    <a class="abs cat-nav" style="left:346px;">Canned Pickles</a>
    <a class="abs cat-nav" style="left:430px;">Cookies</a>
    <a class="abs cat-nav" style="left:486px;">Cheeses</a>
    <a class="abs cat-nav" style="left:542px;">Soaps</a>
  </nav>
  <div class="rule" style="left:0; top:77px; width:708px;"></div>
</header>

<main>
  <h1 class="abs title">Strawberry Jam with Candied Fruits and Condiment Spicy, Made in California</h1>
  <div class="abs price">Price: $12.50</div>
  <a class="abs add-btn">
    <svg width="9" height="7" viewBox="0 0 9 7"><path d="M0 2h9L8 7H1z M2.5 2 4 0 M6.5 2 5 0" fill="#fff" stroke="#fff" stroke-width=".6"/></svg>Add to Cart</a>

  <div class="rule" style="left:66px; top:212px; width:273px;"></div>
  <h2 class="abs section-head" style="left:66px; top:223px;">Overview</h2>
  <ul class="abs bullets" style="left:66px; top:238px;">
    <li>Handmade, Natural and 100% Organic</li>
    <li>Ingredients: Strawberry, Sugar, Natural Spices</li>
    <li>Net Weight: 6OZ (170g)</li>
    <li>No Preservatives</li>
  </ul>

  <div class="rule" style="left:66px; top:290px; width:273px;"></div>
  <h2 class="abs section-head" style="left:66px; top:301px;">Score in Market</h2>
  <ul class="abs bullets" style="left:66px; top:316px;">
    <li><b style="color:#111;">33</b><span class="heart">♥</span>(Favorited by 33 People)</li>
    <li><span class="stars">★★★★★</span>(4.7/5.0 Positive Rating)</li>
  </ul>

  <div class="rule" style="left:66px; top:343px; width:273px;"></div>
  <h2 class="abs section-head" style="left:66px; top:353px;">Description</h2>
  <div class="abs desc">
    <p>&nbsp;Lorem ipsum dolor sit amet, consectetur adipiscing elit. Quisque in est sit amet enim ornare consectetur. Interdum et malesuada fames ac ante ipsum primis in faucibus. Sed viverra ligula ac egestas vestibulum.</p>
    <p>Quisque non ex diam. Praesent quis lacus lacinia ex rhoncus ornare eget sed lacus. Vivamus dignissim vulputate congue. Donec venenatis turpis quam, vestibulum egestas neque aliquet eget. Nam pellentesque metus sodales egestas sagittis. Mauris tincidunt id augue at volutpat.</p>
    <p>Quisque sed felis purus. Duis sodales, dolor sed congue pulvinar, lorem justo dignissim tellus, in laoreet nibh leo vitae neque. Vestibulum ante ipsum primis in faucibus orci luctus et ultrices posuere cubilia Curae; Pellentesque molestie metus semper iaculis laoreet.</p>
    <p>Nunc ultrices blandit velit eget semper. Nam pretium orci eleifend congue suscipit. Nulla libero arcu, pellentesque ac efficitur eu, faucibus ut neque. Suspendisse scelerisque porttitor consectetur. Pellentesque in varius quam.</p>
  </div>
  <a class="abs more">+ More</a>

  <div class="abs hero-photo" role="img" aria-label="Product photo: jar of strawberry jam with fresh strawberries in a garden setting"></div>
  <div class="abs fav"><svg width="11" height="10" viewBox="0 0 11 10"><path d="M5.5 9 1.2 4.8A2.4 2.4 0 0 1 5.5 1.6a2.4 2.4 0 0 1 4.3 3.2z" fill="none" stroke="#ec1f27" stroke-width="1.1"/></svg></div>
  <div class="abs zoom"><svg width="10" height="10" viewBox="0 0 10 10"><circle cx="4" cy="4" r="3" fill="none" stroke="#222" stroke-width="1.2"/><path d="M6.2 6.2 9 9M2.6 4h2.8M4 2.6v2.8" stroke="#222" stroke-width="1.1"/></svg></div>
  <div class="abs thumb t1" role="img" aria-label="Open jar of jam"></div>
  <div class="abs thumb t2" role="img" aria-label="Fresh strawberries"></div>
  <div class="abs thumb t3" role="img" aria-label="Jam on a wooden table"></div>
  <div class="abs thumb t4" role="img" aria-label="Strawberries with leaves"></div>
  <div class="abs thumb t5" role="img" aria-label="Jar of jam with gingham lid"></div>

  <h2 class="abs section-head" style="left:354px; top:453px;">Shipping</h2>
  <ul class="abs bullets ship-item"><li>Ready for ship to US destinations in 2 business days</li></ul>
  <div class="rule" style="left:354px; top:494px; width:304px;"></div>

  <h2 class="abs section-head" style="left:354px; top:512px;">Share with Friends</h2>
  <div class="abs share-icon" style="left:458px; background:#3b5998;" aria-label="Share on Friendnet"></div>
  <div class="abs share-icon" style="left:494px; background:#55acee; border-radius:50%;" aria-label="Share on Chirper"></div>
  <div class="abs" style="left:531px; top:510px;" aria-label="Share by email">
    <svg width="17" height="13" viewBox="0 0 17 13"><rect width="17" height="13" rx="1.5" fill="#ec1f27"/><path d="M1 1.5l7.5 6 7.5-6" fill="none" stroke="#fff" stroke-width="1.3"/></svg></div>
  <div class="rule" style="left:354px; top:541px; width:304px;"></div>

  <h2 class="abs section-head" style="left:354px; top:549px;">Payment Options</h2>
  <div class="abs pay-card" style="left:462px;">Cardmark</div>
  <div class="abs pay-card" style="left:493px;">Vessa</div>
  <div class="abs pay-card" style="left:524px;">PayLoop</div>

  <div class="rule" style="left:149px; top:612px; width:411px;"></div>
  <h2 class="abs similar-head">Similar Products</h2>
  <div class="abs card" style="left:149px;">
    <div class="card-photo" role="img" aria-label="Apricot and strawberry jam jars with toast" style="background:linear-gradient(150deg,#e87a2a,#b0262a 55%,#8a5a34);"></div>
    <div class="card-name">Apricot jam and strawberry jam</div><div class="card-price">$12.55</div></div>
  <div class="abs card" style="left:258px;">
    <div class="card-photo" role="img" aria-label="Physalis jam jar with fruit pieces" style="background:linear-gradient(150deg,#e9e4da,#f08c22 55%,#d9c9a8);"></div>
    <div class="card-name">Physalis jam with big pieces of fruit</div><div class="card-price">$17.20</div></div>
  <div class="abs card" style="left:369px;">
    <div class="card-photo" role="img" aria-label="Raspberry jam in a glass jar" style="background:linear-gradient(150deg,#7fb04a,#c2264f 55%,#f0d7df);"></div>
    <div class="card-name" style="margin-top:9px;">Natural raspberry jam with fruit pieces</div><div class="card-price">$15.99</div></div>
  <div class="abs card" style="left:479px;">
    <div class="card-photo" role="img" aria-label="Cherry jam with fresh cherries on wood" style="background:linear-gradient(150deg,#8a0f1a,#4a1016 55%,#8a6a48);"></div>
    <div class="card-name" style="margin-top:9px;">Cherry jam with fresh cherries</div><div class="card-price">$13.00</div></div>
</main>

<section>
  <div class="abs news-band" role="img" aria-label="Rolling green countryside under a cloudy blue sky"></div>
  <div class="abs news-label">Newsletter</div>
  <div class="abs news-title">Subscribe to our Newsletter</div>
  <div class="abs news-sub">And Get Informed About What's on Offer NOW</div>
  <div class="abs news-form">
    <div class="news-input">Email Address</div>
    <div class="news-btn">Subscribe</div>
  </div>
</section>

<footer>
  <div class="abs footer"></div>
  <div class="abs brand footer-brand"><span>Brindlecove</span><span class="brand-dot"></span></div>
  <div class="abs social" style="left:308px;">FN</div>
  <div class="abs social" style="left:341px;">CH</div>
  <div class="abs social" style="left:374px;">SG</div>
  <div class="abs copyright">Copyright © 2018 Brindlecove. All rights reserved.</div>
</footer>

</body>
</html>
```